Tambrel Couriers Web design

Take a look at our existing website(www.tmbrl-example.com) and design a new one, plus coding and recreate an existing logo.

```html
<!DOCTYPE html>
<html lang="en">
<head>
<meta charset="utf-8">
<title>Tambrel Couriers</title>
<link href="https://fonts.googleapis.com/css2?family=Outfit:wght@300;400;500;600;700&display=swap" rel="stylesheet">
<style>
:root{
  --blue:#0b5cb1;
  --blue-dark:#084a93;
  --orange:#f7901e;
  --ink:#1b1b1f;
  --text:#3d3d45;
  --muted:#8a8f99;
  --light:#f4f4f4;
  --navy:#222a3a;
  --navy-deep:#1a2030;
  --white:#ffffff;
}
*{margin:0;padding:0;box-sizing:border-box}
html,body{width:1200px;height:3614px;overflow:hidden}
body{font-family:"Outfit",sans-serif;color:var(--text);background:var(--white);position:relative}
.abs{position:absolute}
.btn{position:absolute;display:flex;align-items:center;justify-content:center;background:var(--orange);color:var(--white);font-weight:500;font-size:13px;border-radius:20px;text-transform:uppercase}
.brand{font-weight:700;color:var(--blue);font-size:22px;letter-spacing:1px;display:flex;align-items:center;gap:8px;line-height:1}
.brand .mark{width:16px;height:16px;background:var(--orange)}
.brand small{display:block}
/* header */
.topbar{position:absolute;top:0;left:0;width:1200px;height:98px;background:var(--white)}
.contact-mini{position:absolute;left:748px;top:14px;display:flex;gap:8px;align-items:center;font-size:12px;color:var(--ink);line-height:1.2}
.contact-mini b{font-weight:600}
.nav{position:absolute;left:372px;top:57px;width:828px;height:41px;background:var(--blue);clip-path:polygon(20px 0,100% 0,100% 100%,0 100%)}
.nav-edge{position:absolute;left:368px;top:57px;width:24px;height:41px;background:var(--orange);clip-path:polygon(20px 0,24px 0,4px 100%,0 100%)}
.nav a{position:absolute;top:13px;color:var(--white);font-size:11.5px;text-decoration:none;text-transform:uppercase}
.nav a.active{border-bottom:2px solid var(--orange);padding-bottom:3px}
/* hero */
.hero{position:absolute;top:98px;left:0;width:1200px;height:600px;background:linear-gradient(90deg,#eef0ec 0%,#dfe4d9 30%,#c9b79a 60%,#e8dcc9 80%,#b8c6d6 100%)}
.hero-title{position:absolute;left:163px;top:160px;font-size:42px;font-weight:600;color:var(--ink);line-height:49px;text-transform:uppercase}
.hero-title span{color:var(--orange)}
.arrow-btn{position:absolute;width:46px;height:46px;border-radius:50%;display:flex;align-items:center;justify-content:center}
/* about */
.about-block{position:absolute;left:163px;top:865px;width:60px;height:244px;background:var(--blue)}
.about-photo{position:absolute;left:210px;top:806px;width:312px;height:360px;background:linear-gradient(160deg,#f2f2f2,#d9d6d2 60%,#3a3b40)}
.eyebrow{color:var(--blue);font-weight:600;font-size:15px;display:flex;align-items:center;gap:10px}
.eyebrow::before{content:"";width:26px;height:2px;background:var(--orange)}
.about-h{font-size:21px;font-weight:600;color:var(--ink);text-transform:uppercase}
.about-h span{color:var(--orange)}
.lead{font-size:14px;color:var(--ink);line-height:21px;font-weight:500}
.body-p{font-size:12.5px;line-height:21.5px;color:var(--text)}
/* services */
.svc-head{position:absolute;left:435px;top:1281px;width:330px;height:58px;border:3px solid var(--blue);text-align:center}
.svc-head .eye{position:absolute;top:-11px;left:50%;transform:translateX(-50%);background:var(--white);padding:0 8px;color:var(--orange);font-size:16px;font-weight:500;white-space:nowrap;text-transform:uppercase;display:flex;gap:8px;align-items:center}
.svc-head .eye::before,.svc-head .eye::after{content:"";width:22px;height:2px;background:var(--blue)}
.svc-head h2{font-size:32px;font-weight:700;color:var(--ink);line-height:58px;margin-top:1px;text-transform:uppercase}
.svc-photo{position:absolute;width:190px;height:190px;border-radius:50%;border:5px solid var(--orange)}
.svc-icon{position:absolute;width:54px;height:54px;border-radius:50%;background:var(--white);display:flex;align-items:center;justify-content:center;box-shadow:0 2px 6px rgba(0,0,0,.15)}
.svc-card{position:absolute;width:240px;text-align:center;color:var(--white)}
.svc-card h3{font-size:17px;font-weight:600;margin-bottom:8px}
.svc-card p{font-size:11.5px;line-height:18px}
.go{position:absolute;width:30px;height:30px;border-radius:50%;background:rgba(255,255,255,.45);display:flex;align-items:center;justify-content:center}
/* process */
.process{position:absolute;top:1921px;left:0;width:1200px;height:396px;background:var(--light)}
.sec-eye{position:absolute;width:1200px;text-align:center;color:var(--orange);font-size:14px;text-transform:uppercase}
.sec-title{position:absolute;width:1200px;text-align:center;font-size:29px;font-weight:700;color:var(--ink);text-transform:uppercase}
.step{position:absolute;top:179px;width:168px;height:101px;background:var(--white);box-shadow:0 2px 8px rgba(0,0,0,.06);text-align:center;font-size:13px;color:var(--text)}
.step svg{display:block;margin:12px auto 6px}
/* testimonials */
.quote-card{position:absolute;top:2446px;width:348px;height:111px;background:var(--white);box-shadow:0 3px 14px rgba(0,0,0,.07);padding:22px 20px 0 55px;font-size:11.5px;line-height:20px;color:var(--text)}
.quote-card .qm{position:absolute;left:20px;top:14px;font-size:40px;color:var(--blue);font-weight:700;line-height:1}
.person{position:absolute;top:2590px;display:flex;align-items:center;gap:12px}
.avatar{width:40px;height:40px;border-radius:50%;background:radial-gradient(circle at 50% 40%,#e9cdb8,#a98a74)}
.person b{display:block;font-size:11px;font-weight:600;color:var(--ink);text-transform:uppercase}
.person span{font-size:10.5px;color:#a0a4ab}
/* quote form */
.quote-photo{position:absolute;left:0;top:2754px;width:553px;height:450px;background:linear-gradient(135deg,#dfe3ea,#9fb1c6 45%,#e6e6e6 75%,#b9c3cf)}
.quote-panel{position:absolute;left:553px;top:2754px;width:647px;height:450px;background:var(--blue)}
.field{position:absolute;border:1px solid rgba(255,255,255,.35);color:rgba(255,255,255,.85);font-size:10.5px;padding:10px 12px}
/* bottom */
.cta-band{position:absolute;top:3204px;left:0;width:1200px;height:77px;background:var(--navy)}
.footer{position:absolute;top:3281px;left:0;width:1200px;height:270px;background:var(--navy)}
.f-col h4{font-size:16px;font-weight:400;color:var(--white);position:relative;padding-top:0}
.f-col h4::before{content:"";position:absolute;left:0;top:-16px;width:28px;height:2px;background:var(--orange)}
.f-col ul{list-style:none;font-size:11.5px;color:#c9ccd3;line-height:21.5px}
.f-div{position:absolute;top:3330px;width:1px;height:180px;background:rgba(255,255,255,.12)}
.legal{position:absolute;top:3551px;left:0;width:1200px;height:63px;background:var(--navy-deep);color:#aeb3bc;font-size:11px}
</style>
</head>
<body>

<!-- header -->
<header class="topbar">
  <div class="abs brand" style="left:154px;top:38px;flex-direction:column;align-items:flex-start;gap:6px">
    <span style="display:flex;align-items:center;gap:8px"><i class="mark"></i>TAMBREL</span>
    <span style="font-size:16px;padding-left:40px">COURIERS</span>
  </div>
  <div class="contact-mini">
    <svg width="24" height="24" viewBox="0 0 24 24"><path d="M6 3l3 4-2 2c1 3 4 6 7 7l2-2 4 3-2 4C10 21 3 14 3 5z" fill="var(--orange)"/></svg>
    <div><b>0100 555 0199</b><br>info@tmbrl-example.com</div>
  </div>
  <div class="btn" style="left:928px;top:14px;width:110px;height:28px;font-size:11px">Get a quote</div>
  <div class="nav-edge"></div>
  <nav class="nav">
    <a class="active" style="left:41px">Home</a>
    <a style="left:108px">About Us</a>
    <a style="left:198px">Services</a>
    <a style="left:283px">Rates</a>
    <a style="left:351px">Customer Benefits</a>
    <a style="left:501px">Logistics</a>
    <a style="left:594px">Contact Us</a>
  </nav>
</header>

<!-- hero -->
<section class="hero" role="img" aria-label="Courier in a branded cap handing a parcel to a smiling customer signing a clipboard">
  <h1 class="hero-title">Pick-up within<br><span>15–30</span> minutes<br>after call</h1>
  <div class="btn" style="left:163px;top:347px;width:166px;height:37px">Contact us now</div>
  <div class="arrow-btn" style="left:42px;top:238px;background:rgba(247,144,30,.75)"><svg width="16" height="16" viewBox="0 0 16 16"><path d="M10 2L4 8l6 6" stroke="#fff" stroke-width="2.5" fill="none"/></svg></div>
  <div class="arrow-btn" style="left:1111px;top:238px;background:#8a4a10;border:2px solid #fff"><svg width="16" height="16" viewBox="0 0 16 16"><path d="M6 2l6 6-6 6" stroke="#fff" stroke-width="2.5" fill="none"/></svg></div>
  <svg class="abs" style="left:589px;top:524px" width="20" height="42" viewBox="0 0 20 42"><rect x="2" y="1" width="16" height="24" rx="8" stroke="#fff" stroke-width="2" fill="none"/><line x1="10" y1="6" x2="10" y2="11" stroke="#fff" stroke-width="2"/><path d="M10 28v12M6 36l4 4 4-4" stroke="#fff" stroke-width="1.5" fill="none"/></svg>
</section>

<!-- about -->
<section>
  <div class="about-block"></div>
  <div class="about-photo" role="img" aria-label="Smiling office worker in a dark blazer holding a parcel at her desk"></div>
  <div class="abs eyebrow" style="left:580px;top:822px">About Us</div>
  <h2 class="abs about-h" style="left:580px;top:856px">Welcome to <span>Tambrel Couriers.</span></h2>
  <p class="abs lead" style="left:580px;top:893px;width:400px">We are committed to providing professional messenger services to cater for the most important, emergency and time sensitive deliveries valuable to your company.</p>
  <p class="abs body-p" style="left:580px;top:971px;width:400px">Our services range from scheduled local and long distance, same day to all types of On Demand services. Our goal is to become a leader by showing reliability, integrity as well as competitive pricing. Our company is licensed, bonded and fully insured with commercial grade insurance.</p>
  <div class="btn" style="left:580px;top:1099px;width:138px;height:36px">Learn more</div>
</section>

<!-- services -->
<section>
  <div class="svc-head"><div class="eye">Our Services</div><h2>What we do</h2></div>
  <svg class="abs" style="left:0;top:1440px" width="1200" height="481" viewBox="0 0 1200 481"><path d="M0 118 Q600 -120 1200 118 L1200 481 L0 481 Z" fill="var(--blue)"/><path d="M0 118 Q600 -120 1200 118 L1200 481 L0 481 Z" fill="url(#sh)" opacity=".35"/><defs><linearGradient id="sh" x1="0" x2="1"><stop offset="0" stop-color="#3f86cf"/><stop offset=".5" stop-color="#0b5cb1"/><stop offset="1" stop-color="#3f86cf"/></linearGradient></defs></svg>

  <div class="svc-photo" style="left:205px;top:1414px;background:linear-gradient(135deg,#1e3b6e,#6f8fb5,#d9dee6)" role="img" aria-label="Doctor with stethoscope and digital brain scan"></div>
  <div class="svc-photo" style="left:504px;top:1383px;background:linear-gradient(135deg,#e6e2dc,#8c7b6c,#2e2f36)" role="img" aria-label="Business team reviewing papers at a meeting table"></div>
  <div class="svc-photo" style="left:796px;top:1414px;background:linear-gradient(135deg,#d8d6d2,#7b7a7c,#3b3330)" role="img" aria-label="Judge gavel beside legal documents"></div>

  <div class="svc-icon" style="left:273px;top:1576px"><svg width="30" height="30" viewBox="0 0 30 30"><circle cx="15" cy="10" r="6" fill="none" stroke="#555" stroke-width="2"/><path d="M15 7v6M12 10h6" stroke="var(--orange)" stroke-width="2"/><path d="M3 20l6 6h9l8-6M3 20l5-3 6 3" fill="none" stroke="#555" stroke-width="2"/></svg></div>
  <div class="svc-icon" style="left:572px;top:1545px"><svg width="30" height="30" viewBox="0 0 30 30"><circle cx="17" cy="10" r="7" fill="none" stroke="#555" stroke-width="2"/><text x="17" y="14" font-size="10" text-anchor="middle" fill="#555" font-family="Outfit">$</text><path d="M3 20l6 6h9l8-6M3 20l5-3 6 3" fill="none" stroke="var(--orange)" stroke-width="2"/></svg></div>
  <div class="svc-icon" style="left:864px;top:1573px"><svg width="30" height="30" viewBox="0 0 30 30"><rect x="9" y="4" width="12" height="7" rx="1" fill="#555" transform="rotate(-35 15 8)"/><line x1="15" y1="11" x2="22" y2="20" stroke="#555" stroke-width="2.5"/><rect x="4" y="22" width="16" height="4" fill="var(--orange)"/></svg></div>

  <div class="svc-card" style="left:180px;top:1657px"><h3>Hospital &amp; Medical Care</h3><p>Lorem ipsum dolor sit amet in<br>consectetur adipiscing elit Maur<br>in rhoncus orci pellente.</p></div>
  <div class="svc-card" style="left:479px;top:1626px"><h3>Banking &amp; Brokerage</h3><p>Lorem ipsum dolor sit amet in<br>consectetur adipiscing elit Maur<br>in rhoncus orci pellente.</p></div>
  <div class="svc-card" style="left:771px;top:1657px"><h3>Legal Filings</h3><p>Lorem ipsum dolor sit amet in<br>consectetur adipiscing elit Maur<br>in rhoncus orci pellente.</p></div>

  <div class="go" style="left:285px;top:1755px"><svg width="12" height="12" viewBox="0 0 12 12"><path d="M1 6h10M7 2l4 4-4 4" stroke="#fff" stroke-width="1.6" fill="none"/></svg></div>
  <div class="go" style="left:584px;top:1725px"><svg width="12" height="12" viewBox="0 0 12 12"><path d="M1 6h10M7 2l4 4-4 4" stroke="#fff" stroke-width="1.6" fill="none"/></svg></div>
  <div class="go" style="left:876px;top:1755px"><svg width="12" height="12" viewBox="0 0 12 12"><path d="M1 6h10M7 2l4 4-4 4" stroke="#fff" stroke-width="1.6" fill="none"/></svg></div>

  <div class="btn" style="left:530px;top:1808px;width:138px;height:35px">All services</div>
</section>

<!-- process -->
<section class="process">
  <div class="sec-eye" style="top:57px">Our Work Process</div>
  <h2 class="sec-title" style="top:78px">How we work</h2>
  <div class="abs" style="left:580px;top:124px;width:40px;height:2px;background:var(--orange)"></div>
  <svg class="abs" style="left:0;top:130px" width="1200" height="120" viewBox="0 0 1200 120"><g fill="none" stroke="var(--orange)" stroke-width="1.3" stroke-dasharray="3 3"><path d="M330 30 Q380 -5 443 30"/><path d="M755 30 Q810 -5 868 30"/><path d="M545 100 Q600 135 655 100"/></g></svg>
  <div class="step" style="left:194px"><svg width="40" height="46" viewBox="0 0 40 46"><path d="M10 4l6 8-4 4c2 6 7 12 13 14l4-4 8 6-4 7C16 40 4 26 5 9z" fill="var(--blue)"/><path d="M8 30q10 14 26 12" stroke="var(--orange)" stroke-width="2" fill="none"/></svg>Request a Call</div>
  <div class="step" style="left:415px"><svg width="64" height="46" viewBox="0 0 64 46"><rect x="4" y="10" width="36" height="24" fill="var(--orange)"/><path d="M40 16h12l8 10v8H40z" fill="var(--blue)"/><circle cx="22" cy="20" r="7" fill="#fff"/><path d="M22 16v4h3" stroke="var(--blue)" stroke-width="1.5" fill="none"/><circle cx="16" cy="36" r="5" fill="var(--blue)"/><circle cx="50" cy="36" r="5" fill="var(--blue)"/></svg>Pick-up Goods</div>
  <div class="step" style="left:623px"><svg width="50" height="46" viewBox="0 0 50 46"><circle cx="34" cy="12" r="8" fill="none" stroke="var(--orange)" stroke-width="2"/><path d="M34 8v4h3" stroke="var(--blue)" stroke-width="1.5" fill="none"/><path d="M6 16l4 18h18l4 10M12 28h12" stroke="var(--blue)" stroke-width="4" fill="none"/><circle cx="18" cy="10" r="4" fill="var(--orange)"/></svg>WAIT</div>
  <div class="step" style="left:836px"><svg width="46" height="46" viewBox="0 0 46 46"><rect x="14" y="3" width="24" height="22" fill="var(--orange)"/><rect x="24" y="3" width="4" height="10" fill="#fff"/><path d="M4 30l8 0 10 4 12-6 4 3-14 10H4z" fill="var(--blue)"/></svg>Deliver Your Product</div>
</section>

<!-- testimonials -->
<section>
  <h2 class="sec-title" style="top:2373px">What client say</h2>
  <div class="quote-card" style="left:236px"><span class="qm">“</span>The heights by great men reached kept attaine by sudden flight, but the while companion slept were tooiling upward in the night.</div>
  <div class="quote-card" style="left:619px"><span class="qm">“</span>The heights by great men reached kept attaine by sudden flight, but the while companion slept were tooiling upward in the night.</div>
  <svg class="abs" style="left:256px;top:2556px" width="16" height="10"><path d="M0 0h16L8 9z" fill="#fff"/></svg>
  <svg class="abs" style="left:639px;top:2556px" width="16" height="10"><path d="M0 0h16L8 9z" fill="#fff"/></svg>
  <div class="person" style="left:253px"><div class="avatar" role="img" aria-label="Portrait of client Mara Quill"></div><div><b>Mara Quill</b><span>Senior UI/UX Designer</span></div></div>
  <div class="person" style="left:636px"><div class="avatar" role="img" aria-label="Portrait of client Devin Holt"></div><div><b>Devin Holt</b><span>Senior UI/UX Designer</span></div></div>
  <svg class="abs" style="left:582px;top:2684px" width="36" height="10"><circle cx="5" cy="5" r="4" fill="var(--blue)"/><circle cx="17" cy="5" r="3.5" fill="none" stroke="#bbb"/><circle cx="29" cy="5" r="3.5" fill="none" stroke="#bbb"/></svg>
</section>

<!-- request quote -->
<section>
  <div class="quote-photo" role="img" aria-label="Two colleagues in shirts reviewing a tablet at a laptop"></div>
  <div class="quote-panel">
    <div class="abs" style="left:65px;top:68px;font-size:11px;color:rgba(255,255,255,.45)">Book An Appointment</div>
    <h2 class="abs" style="left:71px;top:93px;font-size:26px;font-weight:500;color:#fff">Request A Quote</h2>
    <div class="field" style="left:69px;top:157px;width:156px;height:32px">Your Name</div>
    <div class="field" style="left:241px;top:157px;width:171px;height:32px">Your Email</div>
    <div class="field" style="left:69px;top:205px;width:343px;height:32px">Subject</div>
    <div class="field" style="left:69px;top:251px;width:343px;height:82px">Your Message</div>
    <div class="abs" style="left:66px;top:345px;width:345px;height:32px;background:var(--orange);color:#fff;font-size:10px;font-weight:500;display:flex;align-items:center;justify-content:center;letter-spacing:.5px">SEND REQUEST</div>
  </div>
</section>

<!-- consultation band -->
<section class="cta-band">
  <p class="abs" style="left:248px;top:29px;font-size:17px;color:#fff;font-weight:300">Have any question or <b style="font-weight:600">need any business consultation?</b></p>
  <div class="abs" style="left:841px;top:24px;width:138px;height:34px;background:var(--blue);color:#fff;font-size:10.5px;font-weight:500;display:flex;align-items:center;justify-content:center">CONTACT US NOW!!</div>
</section>

<!-- footer -->
<footer class="footer">
  <div class="abs brand" style="left:180px;top:62px;color:#fff;flex-direction:column;align-items:flex-start;gap:6px">
    <span style="display:flex;align-items:center;gap:8px"><i class="mark"></i>TAMBREL</span>
    <span style="font-size:16px;padding-left:40px">COURIERS</span>
  </div>
  <p class="abs" style="left:180px;top:145px;width:195px;font-size:10.5px;line-height:16px;color:#c9ccd3">Lorem ipsum dolor sit amet, consectetur adipiscing elit. Nullam sollicitudin tempor sem vitae pretium. Fusce ultricies mollis purus non rutrum.</p>

  <div class="f-col abs" style="left:446px;top:67px"><h4>Site Links</h4><ul style="margin-top:18px"><li>Home</li><li>About Us</li><li>Services</li><li>Rates</li><li>Contact Us</li></ul></div>

  <div class="f-col abs" style="left:603px;top:67px;width:200px"><h4>Contact Us</h4>
    <div style="margin-top:22px;font-size:11px;color:#c9ccd3;line-height:16px">
      <div style="display:flex;gap:10px;margin-bottom:14px"><svg width="14" height="14" viewBox="0 0 24 24"><path d="M6 3l3 4-2 2c1 3 4 6 7 7l2-2 4 3-2 4C10 21 3 14 3 5z" fill="none" stroke="#c9ccd3" stroke-width="1.6"/></svg>Phone: 0100 555 0142</div>
      <div style="display:flex;gap:10px;margin-bottom:14px"><svg width="14" height="16" viewBox="0 0 24 28" style="flex:none"><path d="M12 26s-8-9-8-15a8 8 0 0116 0c0 6-8 15-8 15z" fill="none" stroke="#c9ccd3" stroke-width="1.6"/><circle cx="12" cy="11" r="3" fill="none" stroke="#c9ccd3" stroke-width="1.6"/></svg><span>Address: 48 Harlow Lane, Suite 12, Brookmere, BK</span></div>
      <div style="display:flex;gap:10px"><svg width="14" height="14" viewBox="0 0 24 24"><rect x="2" y="5" width="20" height="14" fill="none" stroke="#c9ccd3" stroke-width="1.6"/><path d="M2 5l10 8 10-8" fill="none" stroke="#c9ccd3" stroke-width="1.6"/></svg>Email: mail@tmbrl-example.com</div>
    </div>
  </div>

  <div class="f-col abs" style="left:871px;top:67px"><h4>Get Connected</h4>
    <div style="display:flex;gap:6px;margin-top:12px"><i style="width:20px;height:20px;border-radius:50%;background:var(--blue)"></i><i style="width:20px;height:20px;border-radius:50%;background:var(--blue)"></i><i style="width:20px;height:20px;border-radius:50%;background:var(--blue)"></i></div>
  </div>
  <div class="f-col abs" style="left:871px;top:171px"><h4>Newsletter</h4></div>
  <div class="abs" style="left:871px;top:201px;width:118px;height:27px;background:#fff;font-size:9px;color:#999;padding:8px 10px">Email...</div>
  <div class="abs" style="left:989px;top:201px;width:27px;height:27px;background:var(--blue);display:flex;align-items:center;justify-content:center"><svg width="12" height="12" viewBox="0 0 12 12"><path d="M1 6L11 1 8 11 6 7z" fill="#fff"/></svg></div>
</footer>
<div class="f-div" style="left:393px"></div>
<div class="f-div" style="left:561px"></div>
<div class="f-div" style="left:815px"></div>

<div class="legal">
  <span class="abs" style="left:188px;top:23px">©2021 Tambrel Couriers &nbsp;|&nbsp; All Rights Reserved.</span>
  <span class="abs" style="left:826px;top:23px">Terms &amp; Conditions &nbsp;|&nbsp; Privacy Policy</span>
</div>

</body>
</html>
```